Poster Design for Film: 'Tres Lunas'

Tres Lunas means "two times" in Spanish. This short film is based on the true story of Cuban refugee during the take over of the Ordaz regime in 1959 and how is experiences and stories affected his children and grandchildren. Tres Lunas tells the story of Daniel- a recent grad who is forced to choose between his critically ill grandfather, the business opportunity of a lifetime, and maintaining a relationship with his love interest, Margaret. Through his grandfather's recollections as a young man in 1950's Cuba, Daniel gains a new outlook on life and the things that matter most.

This poster should evoke the drama and truth that the film approaches in a cinematic manner while maintaining the influences of true Cuban culture and history as perceived by a Miami audience today.

For more information please take a look at our fund raising site:
http://www.fundhaven.example/projects/tres-lunas

The grandfather's current life (the Cuban revolutionary/refugee as an old man):
www.clipvault.example/41592867
password: treslunas

A quick teaser of the film, exploring the lives of Daniel (the protagonist; grandson to Cuban refugee/revolutionary) and Meg (Daniel's love interest he neglects to commit to):

http://www.streamtube.example/watch?v=QbRtPwXnLeK

Please let me know if you would like any stills of the film, have any questions, etc. Thanks!

Hey all! So sorry for the delay on the stills- we had some serious technical issues, but now they are up!

Please let me know if you have any questions. We'll be uploaded more stills to choose from tonight.

Thanks!

Hey all!
Unless you need something in specific, I have just uploaded the final stills for the poster. Feel free to use any of the images, but please keep in mind that the main characters are Dan (the grandson), and his grandfather Arturo both young and old. In other words- the three guys.

Please let me know if you have any questions. Thanks! 

Here are some small text details for the bottom of the poster:

A Copper Lantern Production in association with BrightKiln Studios and the Coastal Pines University. Starring Brett Solano, Celina Fuentes, Omar Bustillo, Lucia Ortega, Farid Khoury. Written, Directed, & Produced by Marcos Ibarra. Director of Photography Tomas Varela. Edited by Marcos Ibarra & Tomas Varela.

Hey designers!

I've just uploaded a new still of the main character. Please try to include it in your design, as it is preferred over the other stills of the main character.

Thanks!

I've just uploaded two small logos to be featured on the bottom of the poster.

Thanks!

Target Market(s)

Hollywood. Cuban-Americans. Miamians. Film Critics. Students. Professors.

Adults based in Los Angeles and Miami aged 21-50 that speak English and Spanish and are in the art and entertainment industry.

Industry/Entity Type

Business

Requirements
Must have
• Must evoke the style of Cuba in the late 1950's while staying true to current day culture/style for 20-somethings in America (specifically LA, NYC, Miami).
Nice to have
• A sort of serious, almost stoic style that could possibly evoke a melancholic reaction.
Should not have
• Anything that evokes a daytime soap opera.

```html
<!DOCTYPE html>
<html lang="en">
<head>
<meta charset="utf-8">
<title>Tres Lunas — Film Poster</title>
<link rel="stylesheet" href="https://fonts.googleapis.com/css2?family=Bebas+Neue&display=swap">
<style>
  :root {
    --paper: #f1efea;
    --flag-blue: #1f57a0;
    --flag-blue-deep: #123a73;
    --flag-white: #ecebe7;
    --flag-red: #d23a2a;
    --star: #e9e9e9;
    --ink: #0e0e12;
    --type-light: #ffffff;
    --credit-ink: #3a3a3a;
  }
  * { margin: 0; padding: 0; box-sizing: border-box; }
  html, body {
    width: 800px; height: 1200px; overflow: hidden;
    background: var(--paper);
  }
  .stage {
    position: absolute; left: 0; top: 0;
    width: 864px; height: 1296px;
    transform: scale(0.925926); transform-origin: 0 0;
    background: var(--paper);
  }
  .flag {
    position: absolute; left: 36px; top: 36px;
    width: 792px; height: 1224px;
  }
  .title {
    position: absolute; right: 448px; top: 498px;
    font-family: "Bebas Neue", Impact, sans-serif;
    color: var(--type-light);
    font-size: 168px; line-height: 140px;
    text-align: right; letter-spacing: 2px;
  }
  .director {
    position: absolute; left: 430px; top: 676px;
    font-family: "Bebas Neue", Impact, sans-serif;
    color: var(--type-light);
    text-align: left;
  }
  .director .label { font-size: 24px; line-height: 24px; letter-spacing: 0.5px; }
  .director .name { font-size: 44px; line-height: 40px; }
  .cast {
    position: absolute; right: 448px; top: 800px;
    list-style: none;
    font-family: "Bebas Neue", Impact, sans-serif;
    color: var(--type-light);
    font-size: 32px; line-height: 35px;
    text-align: right; letter-spacing: 0.5px;
  }
  .billing {
    position: absolute; left: 36px; width: 792px; top: 1203px;
    font-family: "Bebas Neue", Impact, sans-serif;
    color: var(--credit-ink);
    font-size: 11.5px; line-height: 17px;
    text-align: center; letter-spacing: 0.2px;
  }
</style>
</head>
<body>
<main class="stage">
  <svg class="flag" viewBox="0 0 792 1224" aria-hidden="false">
    <defs>
      <radialGradient id="wear" cx="50%" cy="45%" r="75%">
        <stop offset="55%" stop-color="#000" stop-opacity="0"/>
        <stop offset="100%" stop-color="#000" stop-opacity="0.35"/>
      </radialGradient>
      <radialGradient id="figure-shade" cx="50%" cy="50%" r="50%">
        <stop offset="0%" stop-color="#0e0e12" stop-opacity="0.85"/>
        <stop offset="70%" stop-color="#0e0e12" stop-opacity="0.6"/>
        <stop offset="100%" stop-color="#0e0e12" stop-opacity="0"/>
      </radialGradient>
      <radialGradient id="smoke" cx="50%" cy="50%" r="50%">
        <stop offset="0%" stop-color="#111" stop-opacity="0.8"/>
        <stop offset="100%" stop-color="#111" stop-opacity="0"/>
      </radialGradient>
    </defs>
    <g class="flag-stripes">
      <rect x="0" y="0" width="792" height="1224" fill="var(--flag-blue)"/>
      <rect x="157" y="0" width="159" height="1224" fill="var(--flag-white)"/>
      <rect x="476" y="0" width="158" height="1224" fill="var(--flag-white)"/>
    </g>
    <polygon class="flag-triangle" points="0,0 792,0 396,644" fill="var(--flag-red)"/>
    <polygon class="flag-star" fill="var(--star)"
      points="404,158 426,218 490,220 440,258 458,320 404,284 350,320 368,258 318,220 382,218"/>
    <rect class="flag-wear" x="0" y="0" width="792" height="1224" fill="url(#wear)"/>
    <g class="portrait" role="img" aria-label="Photograph of the grandfather in dark silhouette, seen in profile with head bowed, fading into ink smoke">
      <ellipse cx="380" cy="520" rx="280" ry="470" fill="url(#figure-shade)"/>
      <ellipse cx="400" cy="960" rx="260" ry="110" fill="url(#smoke)"/>
    </g>
  </svg>

  <h1 class="title">Tres<br>Lunas</h1>

  <div class="director">
    <div class="label">Directed by</div>
    <div class="name">Marcos<br>Ibarra</div>
  </div>

  <ul class="cast">
    <li>Farid Khoury</li>
    <li>Celina Fuentes</li>
    <li>Omar Bustillo</li>
    <li>Brett Solano</li>
    <li>Lucia Ortega</li>
  </ul>

  <footer class="billing">
    <p>A Copper Lantern Production in association with BrightKiln Studios and the Coastal Pines University &nbsp;Starring Brett Solano, Celina Fuentes, Omar Bustillo, Lucia Ortega, Farid Khoury</p>
    <p>Written, Directed &amp; Produced by Marcos Ibarra &nbsp;Director of Photography Tomas Varela &nbsp;Edited by Marcos Ibarra &amp; Tomas Varela.</p>
  </footer>
</main>
</body>
</html>
```